Corporate Design für Sachverständigerbüro
Professionelle und kreative Arbeit. Der Designer geht gut auf die Wünsche der Kunden ein und reagiert schnell.
Zielgruppe
freiberufliche Tätigkeit als öffentlich bestellter und vereidigter Sachverständiger
Erstellung von landwirtschaftlichen und insolvenzspezifischen Gutachten, betriebswirtschaftliche Beratung, Betriebsfortführung, Unternehmensbewertung
Zielgruppe: Insovenzverwalter, Rechtsanwälte, Steuerberater, Landwirte
Aufgabenstellung
Nennung des Names, der öffentlichen Bestellung sowie Sachverständigenbüro Henrik Vosse;
Gerne dunkelgrüne Logoelemente; Logo eher schlicht; Deisign sollte Seriösität, Vertrauen und Fachkompetenz kommunizieren

```html
<!DOCTYPE html>
<html lang="de">
<head>
<meta charset="utf-8">
<title>Sachverständigenbüro Henrik Vosse – Visitenkarten</title>
<link rel="stylesheet" href="https://fonts.googleapis.com/css2?family=EB+Garamond:wght@400;600;700&family=Open+Sans:wght@400&display=swap">
<style>
  :root {
    --page: #f1f1f2;
    --card-light: #d3d2d5;
    --card-mid: #c5c4c7;
    --card-dark: #b3b2b6;
    --green: #034a31;
    --ink: #1c1a1b;
    --gap: #c9c8cb;
  }
  * { margin: 0; padding: 0; box-sizing: border-box; }
  html, body { width: 1200px; height: 842px; overflow: hidden; background: var(--page); }
  .canvas { position: relative; width: 1200px; height: 842px; }

  .card {
    position: absolute;
    background: radial-gradient(ellipse at 55% 30%, var(--card-light), var(--card-mid) 60%, var(--card-dark));
    box-shadow: 3px 4px 6px rgba(0,0,0,.25);
    overflow: hidden;
    font-family: "EB Garamond", Georgia, serif;
    color: var(--ink);
  }
  .card--portrait { width: 252px; height: 388px; top: 46px; }
  .card--landscape { width: 380px; height: 246px; top: 534px; }
  .card--front-portrait { left: 236px; }
  .card--back-portrait { left: 705px; }
  .card--front-landscape { left: 173px; }
  .card--back-landscape { left: 649px; }

  .mark { position: absolute; background: var(--green); }
  .mark-label {
    position: absolute; color: var(--green); font-weight: 600;
    text-align: center; white-space: nowrap;
  }

  .holder-name { position: absolute; font-weight: 700; font-size: 18px; }
  .role { position: absolute; right: 25px; text-align: right; font-size: 12px; line-height: 1.55; }
  .role .job { font-weight: 700; }
  .contact { position: absolute; right: 25px; text-align: right; font-size: 12.5px; line-height: 13.5px; }
  .contact .online { font-weight: 700; }

  .band { position: absolute; left: 0; bottom: 0; width: 100%; height: 15px; display: block; }

  .office { position: absolute; color: var(--ink); }
  .office-type { font-family: "Open Sans", Arial, sans-serif; font-weight: 400; letter-spacing: .16em; display: block; white-space: nowrap; }
  .office-name { font-family: "EB Garamond", Georgia, serif; font-weight: 700; display: block; white-space: nowrap; letter-spacing: .01em; }

  .card--front-portrait .mark { left: 100px; top: 24px; width: 50px; height: 50px; }
  .card--front-portrait .mark-label { left: 76px; top: 78px; width: 98px; font-size: 9px; }
  .card--front-portrait .holder-name { left: 26px; top: 118px; }
  .card--front-portrait .role { top: 168px; }
  .card--front-portrait .contact { top: 261px; }

  .card--back-portrait .mark { left: 82px; top: 137px; width: 86px; height: 86px; }
  .card--back-portrait .office { left: 0; width: 100%; top: 224px; text-align: center; }
  .card--back-portrait .office-type { font-size: 12px; line-height: 14px; }
  .card--back-portrait .office-name { font-size: 19px; line-height: 20px; }

  .card--front-landscape .mark { left: 25px; top: 25px; width: 98px; height: 98px; }
  .card--front-landscape .mark-label { left: 14px; top: 127px; width: 120px; font-size: 11px; }
  .card--front-landscape .holder-name { right: 25px; top: 22px; }
  .card--front-landscape .role { top: 78px; }
  .card--front-landscape .contact { top: 143px; }

  .card--back-landscape .mark { left: 41px; top: 95px; width: 57px; height: 57px; }
  .card--back-landscape .office { left: 109px; top: 100px; }
  .card--back-landscape .office-type { font-size: 16px; line-height: 18px; }
  .card--back-landscape .office-name { font-size: 28px; line-height: 28px; }
</style>
</head>
<body>
<main class="canvas">

  <section class="card card--portrait card--front-portrait" aria-label="Visitenkarte hochformat Vorderseite">
    <div class="mark"></div>
    <div class="mark-label">Henrik Vosse</div>
    <div class="holder-name">Your Name</div>
    <div class="role"><div class="job">Your job</div><div>address</div></div>
    <div class="contact">
      <div>Tel. +49 (0)4321.123-321</div>
      <div>Fax. +49 (0)4321.123-321</div>
      <div>Mob. +49 (0)2345.543-345</div>
      <div class="online">youremail@email.com</div>
      <div class="online">www.yourweb.com</div>
    </div>
    <svg class="band" viewBox="0 0 252 15" preserveAspectRatio="none" aria-hidden="true">
      <rect width="252" height="15" fill="var(--green)"/>
      <polygon points="120,15 133,0 140,0 127,15" fill="var(--gap)"/>
      <polygon points="186,15 199,0 206,0 193,15" fill="var(--gap)"/>
    </svg>
  </section>

  <section class="card card--portrait card--back-portrait" aria-label="Visitenkarte hochformat Rückseite">
    <div class="mark"></div>
    <div class="office">
      <span class="office-type">Sachverständigenbüro</span>
      <span class="office-name">HENRIK VOSSE</span>
    </div>
  </section>

  <section class="card card--landscape card--front-landscape" aria-label="Visitenkarte querformat Vorderseite">
    <div class="mark"></div>
    <div class="mark-label">Henrik Vosse</div>
    <div class="holder-name">Your Name</div>
    <div class="role"><div class="job">Your job</div><div>address</div></div>
    <div class="contact">
      <div>Tel. +49 (0)4321.123-321</div>
      <div>Fax. +49 (0)4321.123-321</div>
      <div>Mob. +49 (0)2345.345-543</div>
      <div class="online">youremail@email.com</div>
      <div class="online">www.yourweb.com</div>
    </div>
    <svg class="band" viewBox="0 0 380 15" preserveAspectRatio="none" aria-hidden="true">
      <rect width="380" height="15" fill="var(--green)"/>
      <polygon points="252,15 265,0 272,0 259,15" fill="var(--gap)"/>
      <polygon points="318,15 331,0 338,0 325,15" fill="var(--gap)"/>
    </svg>
  </section>

  <section class="card card--landscape card--back-landscape" aria-label="Visitenkarte querformat Rückseite">
    <div class="mark"></div>
    <div class="office">
      <span class="office-type">Sachverständigenbüro</span>
      <span class="office-name">HENRIK VOSSE</span>
    </div>
  </section>

</main>
</body>
</html>
```